Oil and gas industry project solutions company needs professional cards with Canadian aboriginal fee

We are a aboriginally owned company that is focused on Project Planning, Management, Inspection & Consulting for Canada's Petroleum Industry. We have a logo that we would like to incorporate into a professional looking business card. We are professionals that offer services from project inception to completion.

Target Market(s)

Major industry leaders like NorvaLine, Brisk, Vorkantrel, Pelquist etc.

Industry/Entity Type

Industry

Contact Information for Business Card

Milo Rensford
milo@orvelpike.ca
250 555 0187

Requirements
Must have
• OrvelPike Inc. logo.
• Address is: RR4, Site2, Comp17 Fort St. John, BC V9X 2K3 Traditional Territory of the Treaty 8 People
• Colors that are in logo
• Banner or picture on back
• Ability to put different names and contacts
• Website: orvelpike.ca
• "Project Planning, Management, Inspection & Consulting for Canada's Petroleum Industry"

```html
<!DOCTYPE html>
<html lang="en">
<head>
<meta charset="utf-8">
<title>OrvelPike Inc. Business Card</title>
<link rel="stylesheet" href="https://fonts.googleapis.com/css2?family=Open+Sans:wght@400;600;700&display=swap">
<style>
  :root {
    --page-bg: #e9e6e1;
    --green: #6cb23e;
    --green-dark: #4f9a2c;
    --white: #ffffff;
    --card-white: #f7f7f7;
    --navy: #2b3470;
    --sky: #7fb0de;
    --machine: #e3b81c;
    --ground: #3a3a34;
  }
  * { margin: 0; padding: 0; box-sizing: border-box; }
  html, body { width: 1200px; height: 843px; overflow: hidden; }
  body {
    background: var(--page-bg);
    font-family: "Open Sans", sans-serif;
    position: relative;
  }
  .card {
    position: absolute;
    left: 270px;
    width: 660px;
    height: 377px;
    border-radius: 16px;
    overflow: hidden;
    box-shadow: 0 6px 18px rgba(0,0,0,0.18);
  }
  .card-back { top: 30px; }
  .card-front { top: 436px; background: var(--card-white); }

  /* Back */
  .site-photo {
    position: absolute; inset: 0;
    background:
      linear-gradient(180deg, var(--sky) 0%, #b9d3ec 38%, transparent 39%),
      linear-gradient(90deg, var(--machine) 0%, #c99e14 45%, #6b6a5a 70%, var(--ground) 100%);
  }
  .back-shade {
    position: absolute; inset: 0;
    background: linear-gradient(90deg, rgba(0,0,0,0) 40%, rgba(0,0,0,0.55) 100%);
  }
  .back-brand {
    position: absolute; right: 44px; top: 150px;
    text-align: right; color: var(--white);
  }
  .back-brand .brand-name { font-size: 40px; font-weight: 700; line-height: 1; }
  .back-brand .brand-site { font-size: 17px; font-weight: 400; letter-spacing: 3px; margin-top: 10px; }

  /* Front */
  .front-swoosh { position: absolute; inset: 0; }
  .holder-name {
    position: absolute; left: 40px; top: 34px;
    color: var(--white); font-size: 21px; font-weight: 700;
  }
  .contact {
    position: absolute; left: 40px; top: 168px;
    color: var(--white); font-size: 15px; line-height: 21px;
  }
  .contact .address { margin-bottom: 4px; }
  .contact li { list-style: none; display: flex; align-items: center; gap: 10px; }
  .contact svg { width: 13px; height: 13px; flex: none; }
  .front-brand {
    position: absolute; left: 392px; top: 244px;
    display: flex; align-items: center; gap: 12px;
  }
  .front-brand .mark {
    width: 34px; height: 34px; border-radius: 50%; background: var(--green);
  }
  .front-brand .brand-name {
    font-size: 31px; font-weight: 700; color: var(--navy); line-height: 1;
  }
</style>
</head>
<body>

<section class="card card-back">
  <div class="site-photo" role="img" aria-label="Photo of yellow pipeline construction machinery and a worker on a site under blue sky"></div>
  <div class="back-shade"></div>
  <div class="back-brand">
    <div class="brand-name">OrvelPike Inc.</div>
    <div class="brand-site">orvelpike.ca</div>
  </div>
</section>

<section class="card card-front">
  <svg class="front-swoosh" viewBox="0 0 660 377" preserveAspectRatio="none" aria-hidden="true">
    <defs>
      <linearGradient id="greenFill" x1="0" y1="0" x2="1" y2="1">
        <stop offset="0" stop-color="#7cc04c"/>
        <stop offset="1" stop-color="#4f9a2c"/>
      </linearGradient>
    </defs>
    <path d="M0,0 H430 C340,60 262,140 252,230 C244,300 270,350 312,377 H0 Z" fill="url(#greenFill)"/>
  </svg>

  <h1 class="holder-name">Milo Rensford</h1>

  <div class="contact">
    <p class="address">RR4, Site2, Comp17 Fort<br>St. John, BC V9X 2K3</p>
    <ul>
      <li>
        <svg viewBox="0 0 16 16"><path fill="#fff" d="M3.6 1.5l2.3 2.6-1.4 1.8c.9 2 2.5 3.6 4.6 4.6l1.8-1.4 2.6 2.3-1.3 2.2C7 13.4 2.6 9 1.4 2.8z"/></svg>
        <span>250 555 0187</span>
      </li>
      <li>
        <svg viewBox="0 0 16 16"><rect x="1" y="3" width="14" height="10" rx="1" fill="#fff"/><path d="M1.5 3.5l6.5 5 6.5-5" fill="none" stroke="#4f9a2c" stroke-width="1.2"/></svg>
        <span>milo@orvelpike.ca</span>
      </li>
      <li>
        <svg viewBox="0 0 16 16"><circle cx="8" cy="8" r="7" fill="#fff"/><path d="M1 8h14M8 1c-3 3-3 11 0 14M8 1c3 3 3 11 0 14" fill="none" stroke="#4f9a2c" stroke-width="1"/></svg>
        <span>www.orvelpike.ca</span>
      </li>
    </ul>
  </div>

  <div class="front-brand">
    <span class="mark"></span>
    <span class="brand-name">OrvelPike Inc.</span>
  </div>
</section>

</body>
</html>
```